Business Card for my building company

I would like the card to make a statement, so as soon as you see the card you think "wow nice card' and then read the details on the card its self. Also i would like to be able to put in the detail for the MUST HAVES so please Crete a box that i can alter depending on who in my business needs the cards. Thank you

Target Market(s)

Any one looking to build a house/ townhouse or duplex

Industry/Entity Type

Home Builder

Contact Information for Business Card

I would like the card to have the logo on the card and the must haves

Font styles to use
Sans Serif

Requirements
Must have
• Name
• Phone Number
• Email Address
• Website
• Licence Number
• Abn

```html
<!DOCTYPE html>
<html lang="en">
<head>
<meta charset="utf-8">
<title>Coastline Builders – Business Card</title>
<link href="https://fonts.googleapis.com/css2?family=Open+Sans:wght@400;600;700&display=swap" rel="stylesheet">
<style>
  :root {
    --backdrop: #2e2724;
    --card-black: #0b0b0b;
    --card-black-soft: #1a1a1a;
    --gold: #d4a846;
    --white: #ffffff;
    --ink: #111111;
  }
  * { margin: 0; padding: 0; box-sizing: border-box; }
  html, body {
    width: 1200px; height: 844px; overflow: hidden;
    background: var(--backdrop);
    font-family: "Open Sans", sans-serif;
  }
  .stage {
    position: relative; width: 1200px; height: 844px;
    display: flex; align-items: center; justify-content: center; gap: 50px;
  }
  .card {
    position: relative; width: 520px; height: 300px; overflow: hidden;
    box-shadow: 0 10px 30px rgba(0,0,0,0.45);
  }

  /* Contact side */
  .card-contact {
    background: linear-gradient(100deg, var(--card-black-soft) 0%, var(--card-black) 55%, #000 100%);
    color: var(--white);
  }
  .band { position: absolute; left: 0; right: 0; background: var(--gold); }
  .band-top { top: 0; height: 10px; }
  .band-bottom { bottom: 0; height: 16px; }
  .contact-block {
    position: absolute; left: 0; right: 0; top: 62px;
    text-align: center;
  }
  .person-name {
    color: var(--gold); font-weight: 600; font-size: 17px; letter-spacing: 0.2px;
    margin-bottom: 28px;
  }
  .contact-list { list-style: none; font-size: 13px; line-height: 20px; }
  .contact-list li { display: flex; justify-content: center; align-items: center; gap: 6px; }
  .contact-list svg { width: 10px; height: 10px; fill: var(--gold); }
  .registrations { margin-top: 20px; font-size: 13.5px; line-height: 20px; }
  .registrations .label { color: var(--gold); font-weight: 600; }

  /* Logo side */
  .card-logo { background: var(--white); }
  .edge-tab { position: absolute; width: 26px; height: 36px; background: var(--gold); }
  .edge-tab::after {
    content: ""; position: absolute; top: 0; bottom: 0; width: 4px; background: var(--ink);
  }
  .edge-tab-right { right: 0; top: 56px; }
  .edge-tab-right::after { left: 0; }
  .edge-tab-left { left: 0; bottom: 66px; }
  .edge-tab-left::after { right: 0; }
  .brand {
    position: absolute; inset: 0;
    display: flex; align-items: center; justify-content: center; gap: 12px;
  }
  .brand-mark { width: 30px; height: 30px; background: var(--gold); }
  .brand-name {
    color: var(--ink); font-weight: 700; font-size: 30px; letter-spacing: 0.5px;
  }
</style>
</head>
<body>
<main class="stage">
  <section class="card card-contact" aria-label="Business card contact side">
    <div class="band band-top"></div>
    <div class="contact-block">
      <p class="person-name">Marcus Hale</p>
      <ul class="contact-list">
        <li>
          <svg viewBox="0 0 10 10" aria-hidden="true"><path d="M2 0.5 L3.6 2.6 L2.8 3.6 Q4 6 6.4 7.2 L7.4 6.4 L9.5 8 L8.6 9.5 Q4.5 9.5 0.5 1.4 Z"/></svg>
          <span>(044)-555-0192</span>
        </li>
        <li>
          <svg viewBox="0 0 10 10" aria-hidden="true"><path d="M0.5 2 H9.5 V8.5 H0.5 Z M1 2.4 L5 5.6 L9 2.4" stroke="#0b0b0b" stroke-width="0.8"/></svg>
          <span>hello@coastlinebuild.com</span>
        </li>
        <li>
          <svg viewBox="0 0 10 10" aria-hidden="true"><circle cx="5" cy="5" r="4.6"/><path d="M0.6 5 H9.4 M5 0.4 Q2.4 5 5 9.6 M5 0.4 Q7.6 5 5 9.6" stroke="#0b0b0b" stroke-width="0.7" fill="none"/></svg>
          <span>www.coastlinebuild.com</span>
        </li>
      </ul>
      <div class="registrations">
        <p><span class="label">Licence Number :</span> 123 456 789</p>
        <p><span class="label">Abn :</span> 123 456 789</p>
      </div>
    </div>
    <div class="band band-bottom"></div>
  </section>

  <section class="card card-logo" aria-label="Business card logo side">
    <div class="edge-tab edge-tab-right"></div>
    <div class="edge-tab edge-tab-left"></div>
    <div class="brand">
      <span class="brand-mark" aria-hidden="true"></span>
      <span class="brand-name">Coastline Builders</span>
    </div>
  </section>
</main>
</body>
</html>
```